Block makes the buck for writing

We need a notepad in DIN A4 format which we can give to our customers at events. We, KORVANE, are active in the field of safe electrical engineering and offer software, hardware, academia and consulting in this field. With our software can be z. For example, you can quickly and easily inventory and document all equipment and equipment. Every tool must be checked in Germany and the test repeated at regular intervals. The appropriate test specifications are stored in our software. In addition to the software, we also offer measuring and testing equipment. In our academy, we also offer seminars on various areas of safe electrical engineering. Our consulting advises companies on the establishment of a legally compliant company organization. If necessary, our experts also take on the temporary function of external responsible electrician. So we offer an all-round package concerning safe electrical engineering. KORVANE makes working with electricity safe. Every year we offer an event with different workshops. There the users of our software are invited. You can exchange ideas with our lecturers and experts and exchange experiences and tips with each other. For this event we need a writing pad where participants can take their notes throughout the day. In addition, the block should also be used by customers. But it would be nice if he had a special feature / a special feature by which he is particularly happy to use. As basic the block should be branded with our logo and our URL (korvane.de).

```html
<!DOCTYPE html>
<html lang="en">
<head>
<meta charset="utf-8">
<title>KORVANE Notepad</title>
<link rel="stylesheet" href="https://fonts.googleapis.com/css2?family=Barlow+Semi+Condensed:wght@600&family=Roboto:wght@400&display=swap">
<style>
  :root {
    --backdrop: #6f6f6f;
    --paper: #efefef;
    --ink: #4a4a48;
    --ink-soft: #5a5a5a;
    --accent: #f39a2b;
    --rule: #8a8a8a;
    --mark-faint: rgba(200, 200, 200, 0.35);
  }
  html, body {
    margin: 0;
    padding: 0;
    width: 1200px;
    height: 837px;
    overflow: hidden;
    background: var(--backdrop);
  }
  .canvas {
    position: relative;
    width: 1200px;
    height: 837px;
  }
  .sheet {
    position: absolute;
    top: 78px;
    width: 489px;
    height: 692px;
    background: var(--paper);
    overflow: hidden;
  }
  .sheet--cover { left: 76px; }
  .sheet--notes { left: 637px; }

  .brand {
    position: absolute;
    display: flex;
    align-items: center;
    font-family: "Barlow Semi Condensed", "Arial Narrow", sans-serif;
    font-weight: 600;
    color: var(--ink);
    letter-spacing: 0.5px;
    white-space: nowrap;
  }
  .brand__dot {
    border-radius: 50%;
    background: var(--accent);
    flex: none;
  }
  .brand--cover {
    left: 0;
    right: 0;
    top: 290px;
    justify-content: center;
    font-size: 56px;
    gap: 22px;
  }
  .brand--cover .brand__dot { width: 72px; height: 72px; }
  .brand--header {
    left: 48px;
    top: 62px;
    font-size: 24px;
    gap: 9px;
  }
  .brand--header .brand__dot { width: 28px; height: 28px; }

  .cover-url {
    position: absolute;
    left: 0;
    right: 0;
    top: 658px;
    text-align: center;
    font-family: "Roboto", Arial, sans-serif;
    font-size: 7px;
    letter-spacing: 3.2px;
    color: var(--ink-soft);
  }

  .contact {
    position: absolute;
    left: 369px;
    top: 64px;
    margin: 0;
    padding: 0;
    list-style: none;
    font-family: "Roboto", Arial, sans-serif;
    font-size: 7px;
    line-height: 9.5px;
    color: var(--ink-soft);
  }
  .contact li { display: flex; align-items: center; gap: 5px; }
  .contact svg { width: 7px; height: 7px; flex: none; }

  .watermark {
    position: absolute;
    left: 100px;
    top: 230px;
    width: 290px;
    height: 290px;
    border-radius: 50%;
    background: var(--mark-faint);
  }

  .ruling {
    position: absolute;
    left: 41px;
    top: 132px;
    width: 412px;
    margin: 0;
    padding: 0;
    list-style: none;
  }
  .ruling li {
    height: 28px;
    border-top: 1px solid var(--rule);
    box-sizing: border-box;
  }
  .ruling li:last-child { height: 0; }

  .address {
    position: absolute;
    left: 0;
    right: 0;
    top: 663px;
    display: flex;
    justify-content: center;
    align-items: center;
    gap: 4px;
    font-family: "Roboto", Arial, sans-serif;
    font-size: 7px;
    color: var(--ink-soft);
  }
  .address svg { width: 7px; height: 9px; }
</style>
</head>
<body>
<div class="canvas">

  <section class="sheet sheet--cover" aria-label="Notepad cover">
    <div class="brand brand--cover">
      <span class="brand__name">KORVANE</span>
      <span class="brand__dot"></span>
    </div>
    <div class="cover-url">www.korvane.de</div>
  </section>

  <section class="sheet sheet--notes" aria-label="Notepad writing page">
    <div class="watermark"></div>

    <div class="brand brand--header">
      <span class="brand__name">KORVANE</span>
      <span class="brand__dot"></span>
    </div>

    <ul class="contact">
      <li>
        <svg viewBox="0 0 10 10"><path d="M2 0.8 L3.6 0.5 L4.4 2.8 L3.3 3.6 Q4.2 5.8 6.4 6.7 L7.2 5.6 L9.5 6.4 L9.2 8 Q8.6 9.6 6.8 9.2 Q1.6 7.8 0.8 2.8 Q0.6 1.2 2 0.8 Z" fill="#f39a2b"/></svg>
        369-215-4170
      </li>
      <li>
        <svg viewBox="0 0 10 10"><rect x="0.5" y="2" width="9" height="6.5" fill="#f39a2b"/><path d="M0.5 2 L5 5.6 L9.5 2" fill="none" stroke="#efefef" stroke-width="0.9"/></svg>
        info@korvane.de
      </li>
      <li>
        <svg viewBox="0 0 10 10"><circle cx="5" cy="5" r="4.4" fill="none" stroke="#f39a2b" stroke-width="1.2"/><path d="M0.8 5 H9.2 M5 0.6 Q2.6 5 5 9.4 M5 0.6 Q7.4 5 5 9.4" fill="none" stroke="#f39a2b" stroke-width="0.8"/></svg>
        www.korvane.de
      </li>
    </ul>

    <ul class="ruling" aria-hidden="true">
      <li></li><li></li><li></li><li></li><li></li><li></li><li></li><li></li><li></li><li></li>
      <li></li><li></li><li></li><li></li><li></li><li></li><li></li><li></li><li></li>
    </ul>

    <div class="address">
      <svg viewBox="0 0 8 11"><path d="M4 0.3 A3.7 3.7 0 0 1 7.7 4 Q7.7 6.4 4 10.7 Q0.3 6.4 0.3 4 A3.7 3.7 0 0 1 4 0.3 Z" fill="#f39a2b"/><circle cx="4" cy="4" r="1.4" fill="#efefef"/></svg>
      <span>418 Harbor Lane,&nbsp; Fairview, Alaska 34510</span>
    </div>
  </section>

</div>
</body>
</html>
```